Home inspection business! professional look attracting customers just by looks. Read must haves

its a new business I started on my own for home inspections I would like something very professional to give to real estate agents and clients, its going to have my license number on it my business phone number my name my website as well etc on the back side it will be servicing areas and also what kind of services I offer I also have a business card from someone else the way I would like mine to be. I will attach my logo

Home Inspection

listed in nice to haves

• phone number - 555 293 8471
• website- hollowpinecheck.com
• license number #2938475610
• my name Gavin keropulis
• picture of my logo and me on the front
• on the back of the card. stating I am servicing All of New York and Long Island
• also services I will offer will be home inspection -mold inspection -lead inspection -radon inspection -Termite Inspection -Infared Scan.
• and also we provide inspections for single family homes condos co-ops town-homes
• and commercial property
• same colors as the logos and also if you recommend fonts to look like the logo not sure up to you

```html
<!DOCTYPE html>
<html lang="en">
<head>
<meta charset="utf-8">
<title>Hollow Pine Check Home Inspectors – Business Card</title>
<link href="https://fonts.googleapis.com/css2?family=Poppins:wght@400;500&display=swap" rel="stylesheet">
<style>
  :root {
    --backdrop: #e6e1d8;
    --navy: #0b2d4f;
    --sky: #4fa0dc;
    --sky-light: #5aaee8;
    --steel: #7d8389;
    --ink: #4a4f55;
    --white: #ffffff;
    --photo-a: #c9d3dc;
    --photo-b: #6f8296;
  }
  * { margin: 0; padding: 0; box-sizing: border-box; }
  html, body { width: 1200px; height: 900px; overflow: hidden; }
  body {
    position: relative;
    background: var(--backdrop);
    font-family: "Poppins", Arial, sans-serif;
  }
  .card {
    position: absolute;
    left: 311px;
    width: 577px;
    height: 329px;
    box-shadow: 0 6px 14px rgba(0,0,0,0.22);
  }
  .card--front { top: 98px; background: var(--navy); }
  .card--back { top: 472px; background: var(--white); }

  .brand {
    position: absolute;
    display: flex;
    align-items: center;
    gap: 12px;
    color: var(--steel);
    font-weight: 500;
    text-transform: uppercase;
    line-height: 1.15;
  }
  .brand__dot { border-radius: 50%; background: var(--steel); flex: none; }
  .card--front .brand { left: 0; right: 0; top: 170px; justify-content: center; font-size: 25px; }
  .card--front .brand__dot { width: 34px; height: 34px; }
  .brand__sub { display: block; font-size: 0.62em; letter-spacing: 0.3em; }

  .service-list {
    position: absolute;
    left: 0; right: 0; top: 272px;
    text-align: center;
    color: var(--sky-light);
    font-size: 14.5px;
    letter-spacing: 0.04em;
    line-height: 17px;
  }

  .card--back .brand { left: 34px; top: 108px; font-size: 18px; gap: 8px; }
  .card--back .brand__dot { width: 22px; height: 22px; }
  .service-area {
    position: absolute; left: 34px; top: 183px;
    color: var(--sky); font-size: 13.5px; font-weight: 500;
  }
  .divider {
    position: absolute; left: 283px; top: 42px;
    width: 2px; height: 202px; background: var(--sky);
  }
  .portrait {
    position: absolute; left: 312px; top: 41px;
    width: 100px; height: 100px; border-radius: 50%;
    background: radial-gradient(circle at 50% 40%, var(--photo-a), var(--photo-b));
  }
  .inspector {
    position: absolute; left: 311px; top: 154px;
  }
  .inspector__name { color: var(--sky); font-size: 15px; font-weight: 500; letter-spacing: 0.02em; }
  .inspector__license { color: var(--ink); font-size: 13.5px; margin-top: 1px; }
  .contact {
    position: absolute; left: 311px; top: 206px;
    list-style: none; color: var(--ink); font-size: 14px;
  }
  .contact li { display: flex; align-items: center; gap: 9px; height: 23px; }
  .contact svg { width: 16px; height: 16px; fill: var(--sky); }
  .property-band {
    position: absolute; left: 0; bottom: 0;
    width: 100%; height: 60px; background: var(--sky);
    display: flex; align-items: center; justify-content: center;
    text-align: center; color: var(--white);
    font-size: 13px; font-weight: 500; line-height: 18px;
  }
</style>
</head>
<body>
  <section class="card card--front">
    <div class="brand">
      <span class="brand__dot"></span>
      <span>Hollow Pine Check<span class="brand__sub">Home Inspectors</span></span>
    </div>
    <p class="service-list">
      HOME INSPECTION • MOLD INSPECTION • LEAD INSPECTION<br>
      RADON INSPECTION • TERMITE INSPECTION • INFARED SCAN
    </p>
  </section>

  <section class="card card--back">
    <div class="brand">
      <span class="brand__dot"></span>
      <span>Hollow Pine Check<span class="brand__sub">Home Inspectors</span></span>
    </div>
    <p class="service-area">All of New York and Long Island</p>
    <div class="divider"></div>
    <div class="portrait" role="img" aria-label="Portrait photo of the inspector"></div>
    <div class="inspector">
      <p class="inspector__name">GAVIN KEROPULIS</p>
      <p class="inspector__license">LIC NO : #2938475610</p>
    </div>
    <ul class="contact">
      <li>
        <svg viewBox="0 0 24 24" aria-hidden="true"><path d="M6.6 10.8a15.1 15.1 0 0 0 6.6 6.6l2.2-2.2c.3-.3.7-.4 1-.2 1.1.4 2.3.6 3.6.6.6 0 1 .4 1 1V20c0 .6-.4 1-1 1A17 17 0 0 1 3 4c0-.6.4-1 1-1h3.5c.6 0 1 .4 1 1 0 1.3.2 2.5.6 3.6.1.3 0 .7-.2 1z"/></svg>
        555 293 8471
      </li>
      <li>
        <svg viewBox="0 0 24 24" aria-hidden="true"><path d="M12 2a10 10 0 1 0 0 20 10 10 0 0 0 0-20zm6.9 6h-3a15.6 15.6 0 0 0-1.4-3.6A8 8 0 0 1 18.9 8zM12 4c.8 1.2 1.5 2.5 1.9 4h-3.8c.4-1.5 1.1-2.8 1.9-4zM4.3 14a8 8 0 0 1 0-4h3.4a16 16 0 0 0 0 4zm.8 2h3a15.6 15.6 0 0 0 1.4 3.6A8 8 0 0 1 5.1 16zm3-8h-3a8 8 0 0 1 4.3-3.6C8.9 5.5 8.4 6.7 8.1 8zM12 20c-.8-1.2-1.5-2.5-1.9-4h3.8c-.4 1.5-1.1 2.8-1.9 4zm2.3-6H9.7a14.7 14.7 0 0 1 0-4h4.6a14.7 14.7 0 0 1 0 4zm.3 5.6c.6-1.1 1.1-2.3 1.4-3.6h3a8 8 0 0 1-4.4 3.6zm1.7-5.6a16 16 0 0 0 0-4h3.4a8 8 0 0 1 0 4z"/></svg>
        www.hollowpinecheck.com
      </li>
    </ul>
    <div class="property-band">
      <p>SINGLE FAMILY HOMES, CONDOS, CO-OPS TOWN-HOMES<br>AND COMMERCIA PROPERTY</p>
    </div>
  </section>
</body>
</html>
```